Company Binded Folder Showcasing Services

We are wanting to create a presentation folder for potential customers seeking Concrete restoration, painting, waterproofing and more in Florida.
We would like presentation folder to have the following:
Color Scheme: Light or dark Gray, Black, Red, White (We are gravitating towards a darker color scheme)
Front of the folder and the back of the folder to have a symmetrical design with a large picture across (will send pictures as design goes on)
Front of folder should have logo, "25 years" logo, licensed and Insured with General Contractors number
Back of folder should have website, phone number, address, services/specialties listed

When the folder is opened...
The left side should have:
a pocket to put papers in
A business card insert

The right side should have tabs that are embedded in the folder. These tabs/sheets are going to be different sizes so titles along the edges can be visible (a picture can be sent for a visual)
We would like the tab colors to be red
Tab 1: Intro (Smallest Tab/Sheet)
Verbiage and pictures will be sent.
Tab 2: Railing Systems (Larger than tab 1)
Front and back of sheet used for small descriptions, testimonials and pictures.
Tab 3: Painting (Larger than Tab 2)
Verbiage and pictures will be sent
Tab 4: Concrete Restoration (Larger than Tab 3)
Tab 5: Waterproofing and Deck Systems (Largest Tab)
There will be a pocket on the right side of the folder to insert contracts/papers and another business card insert.

Target Market(s)

Property Managers, Building owners that have high rises, hospitality industrial or commercial buildings (especially near the ocean) along the coast of Florida. The company is located in Pompano Beach, but can travel.

Font styles to use
Other font styles liked:
• Match attached custom to complement logo

Colors
ec1f27

Requirements
Must have
• A clean, modern look.
• Pocket for sheets of paper and business card insert (on pocket) on both sides
• Embedded sheets into the folder that have titles along the edges with each sheet having different sizes to showcase services.
Nice to have
• Different designs for owner to choose from
• Darker color schemes
• Pictures edited if necessary to create a sharper image
Should not have
• No watermarks

```html
<!DOCTYPE html>
<html lang="en">
<head>
<meta charset="utf-8">
<title>Corvell's Painting &amp; Restoration – Presentation Folder</title>
<link href="https://fonts.googleapis.com/css2?family=Oswald:wght@500;700&family=Open+Sans:wght@400;600;700&family=Libre+Baskerville&family=Dancing+Script:wght@600&display=swap" rel="stylesheet">
<style>
:root{
  --red:#ec1f27;
  --red-deep:#a3111a;
  --red-dark:#6e0a10;
  --black:#141414;
  --charcoal:#2a2a2a;
  --paper:#ffffff;
  --paper-gray:#e4e4e4;
  --stage:#bdbdbd;
  --label-gray:#8a8a8a;
  --head:'Oswald',sans-serif;
  --body:'Open Sans',sans-serif;
  --serif:'Libre Baskerville',serif;
  --script:'Dancing Script',cursive;
}
*{box-sizing:border-box;margin:0;padding:0}
html,body{width:990px;height:1200px;overflow:hidden}
body{background:var(--stage);position:relative;font-family:var(--body);color:var(--black)}

.spread{position:absolute;left:75px;width:840px;height:500px;box-shadow:0 14px 30px rgba(0,0,0,.35);overflow:hidden}
.spread--outside{top:30px}
.spread--inside{top:560px}
.spread__art{position:absolute;inset:0;width:840px;height:500px}

/* ---------- outside: back panel ---------- */
.specialties{position:absolute;left:16px;top:30px;color:#fff}
.specialties__title{font-family:var(--body);font-weight:700;font-size:10px;color:var(--red);letter-spacing:.2px;margin-bottom:6px}
.specialties__list{list-style:none}
.specialties__list li{display:flex;align-items:center;gap:6px;font-size:11px;line-height:15px}
.tick{width:10px;height:10px;flex:none}

.contact{position:absolute;left:26px;top:318px;font-style:normal}
.contact__company{font-family:var(--body);font-weight:700;font-size:12.5px;margin-bottom:4px;white-space:nowrap}
.contact__row{display:flex;align-items:center;gap:7px;font-size:11.5px;font-weight:600;line-height:17px;white-space:nowrap}
.contact__row--indent{padding-left:18px}
.contact__icon{width:11px;height:11px;flex:none}
.web{position:absolute;top:460px;display:flex;align-items:center;gap:9px;font-family:var(--body);font-weight:700;font-size:17px;letter-spacing:.8px;white-space:nowrap}
.web--back{left:26px}
.web--front{left:446px}
.web__globe{width:20px;height:20px;flex:none}

/* ---------- outside: front panel ---------- */
.tagline{position:absolute;right:22px;top:18px;text-align:right;font-family:var(--serif);font-size:19px;line-height:23px;color:#fff}
.anniversary-seal{position:absolute;right:36px;top:78px;width:70px;height:70px}
.brand-name{position:absolute;right:26px;top:316px;text-align:right;font-family:var(--head);font-weight:700;color:var(--red);text-transform:uppercase;line-height:1}
.brand-name__main{font-size:46px;letter-spacing:2px}
.brand-name__sub{font-size:17px;letter-spacing:2.5px;margin-top:4px}
.license-band{position:absolute;left:460px;top:412px;width:380px;height:22px;background:var(--red);color:#fff;font-family:var(--head);font-weight:500;font-size:13px;line-height:22px;text-align:center;letter-spacing:.5px}

/* ---------- inside: shared ---------- */
.panel{position:absolute;top:0;width:420px;height:500px;overflow:hidden}
.panel--left{left:0;background:linear-gradient(180deg,#eeeeee,#d6d6d6)}
.panel--right{left:420px;background:var(--charcoal)}
.panel--left::after{content:"";position:absolute;right:0;top:0;width:16px;height:100%;background:linear-gradient(90deg,rgba(0,0,0,0),rgba(0,0,0,.25))}

.sheet{position:absolute;background:var(--paper);box-shadow:0 2px 8px rgba(0,0,0,.3)}
.sheet__tab{position:absolute;left:0;right:0;top:0;height:34px;display:flex}
.sheet__brand{flex:0 0 46%;background:var(--paper);border-bottom:3px solid var(--red);font-family:var(--head);font-weight:700;color:var(--red);font-size:13px;line-height:1.05;padding:5px 8px;text-transform:uppercase}
.sheet__brand small{display:block;font-size:7px;letter-spacing:1px}
.sheet__title{flex:1;background:linear-gradient(90deg,var(--black),var(--red-dark) 45%,var(--red));color:#fff;font-family:var(--head);font-weight:500;font-size:15px;letter-spacing:.5px;display:flex;align-items:center;justify-content:center;text-transform:uppercase}
.sheet__heading{position:absolute;font-family:var(--script);font-weight:600;color:var(--red);font-size:22px}
.sheet__text{position:absolute;font-size:7.4px;line-height:10.5px;color:#555;text-align:justify}
.sheet__photo{position:absolute;border:3px solid var(--red);border-radius:14px 4px 14px 4px}

.sheet--painting{left:22px;top:18px;width:330px;height:320px}
.sheet--restoration{left:38px;top:54px;width:340px;height:320px}
.sheet--deck{left:14px;top:92px;width:366px;height:340px}
.sheet--deck .sheet__heading{left:16px;top:42px}
.sheet--deck .sheet__text{left:16px;top:76px;width:180px}
.sheet--deck .sheet__photo{left:206px;top:44px;width:146px;height:206px;background:linear-gradient(180deg,#8fb8dc 0%,#3b5d80 45%,#1f2b3a 100%)}

.pocket{position:absolute;left:0;right:0;bottom:0;height:160px;background:linear-gradient(160deg,var(--red-deep),var(--red-dark) 60%,#3d060a)}
.pocket::before{content:"";position:absolute;left:0;right:0;top:0;height:4px;background:rgba(0,0,0,.35)}

.card{position:absolute;background:var(--paper);box-shadow:0 2px 6px rgba(0,0,0,.4)}
.card--promo{left:110px;top:30px;width:190px;height:108px;text-align:center;padding-top:10px}
.card__name{font-family:var(--head);font-weight:700;color:var(--red);text-transform:uppercase;line-height:1.05}
.card--promo .card__name{font-size:19px}
.card--promo .card__name span{display:block;font-size:9px;letter-spacing:1.5px}
.card__tag{font-family:var(--serif);font-size:7px;color:#333;margin-top:4px}
.card__dot{display:inline-block;width:12px;height:12px;border-radius:50%;border:1.5px solid var(--red);margin-top:3px}
.card__list{font-size:5px;color:#444;line-height:7.5px;margin-top:2px;white-space:nowrap}
.card__list b{color:var(--red)}

/* ---------- inside: right panel tabs ---------- */
.tab{position:absolute;left:0;width:420px;height:46px;background:linear-gradient(90deg,#1a0709 0%,#3a0a0f 30%,var(--red-deep) 65%,var(--red) 100%);box-shadow:0 -3px 6px rgba(0,0,0,.45);color:#fff;font-family:var(--head);font-weight:500;font-size:16px;letter-spacing:.5px;text-transform:uppercase;display:flex;align-items:flex-start;padding-top:8px}
.tab--waterproofing{top:0;padding-left:40px}
.tab--concrete{top:40px;padding-left:86px}
.tab--painting{top:80px;padding-left:140px}
.tab--railing{top:120px;padding-left:120px}
.tab--intro{top:160px;padding-left:150px}

.intro-sheet{position:absolute;left:0;top:196px;width:420px;height:304px;background:linear-gradient(180deg,#f7f7f7,#e6e6e6);box-shadow:0 -3px 6px rgba(0,0,0,.4)}
.intro-sheet .sheet__heading{left:24px;top:22px}
.intro-sheet .sheet__text{left:24px;top:56px;width:190px}
.intro-sheet .sheet__photo{left:236px;top:10px;width:166px;height:110px;background:linear-gradient(160deg,#5f86b8 0%,#2c4a73 50%,#16263d 100%)}

.card--contact{left:200px;top:34px;width:192px;height:104px;overflow:hidden}
.card__wedge{position:absolute;left:0;top:0;width:192px;height:104px}
.card__person{position:absolute;left:10px;top:60px;color:#fff;font-size:8px;font-weight:700;line-height:9px}
.card__person small{display:block;font-weight:400;font-size:5.5px;line-height:7px}
.card--contact .card__name{position:absolute;left:86px;top:10px;font-size:12px;text-align:left}
.card--contact .card__name span{display:block;font-size:6px;letter-spacing:1px}
.card__details{position:absolute;left:96px;top:40px;font-size:5.5px;line-height:8px;color:#333;white-space:nowrap}
.card__details i{display:inline-block;width:4px;height:4px;border-radius:50%;background:var(--red);margin-right:3px;vertical-align:middle}

/* ---------- presentation footer ---------- */
.board-label{position:absolute;left:52px;top:1116px;font-family:var(--body);font-weight:700;font-size:40px;color:var(--label-gray);letter-spacing:1px}
.board-brand{position:absolute;right:70px;top:1086px;text-align:center;font-family:var(--head);font-weight:700;color:var(--red);text-transform:uppercase;line-height:1}
.board-brand__main{font-size:52px;letter-spacing:3px}
.board-brand__sub{font-size:18px;letter-spacing:3px;margin-top:4px}
</style>
</head>
<body>

<section class="spread spread--outside" aria-label="Folder outside: back and front cover">
  <svg class="spread__art" viewBox="0 0 840 500">
    <defs>
      <linearGradient id="paperGrad" x1="0" y1="0" x2="0" y2="1">
        <stop offset="0" stop-color="#ffffff"/><stop offset="1" stop-color="#dedede"/>
      </linearGradient>
      <linearGradient id="redGrad" x1="0" y1="0" x2="1" y2="1">
        <stop offset="0" stop-color="#ec1f27"/><stop offset="1" stop-color="#8d0d14"/>
      </linearGradient>
      <linearGradient id="photoGrad" x1="0" y1="0" x2="0" y2="1">
        <stop offset="0" stop-color="#6fb0e0"/><stop offset=".45" stop-color="#b7c7d3"/>
        <stop offset=".6" stop-color="#9a6a55"/><stop offset=".8" stop-color="#4f6b4a"/>
        <stop offset="1" stop-color="#6e6b78"/>
      </linearGradient>
    </defs>
    <rect width="840" height="500" fill="url(#paperGrad)"/>
    <polygon points="0,0 300,0 0,250" fill="#141414"/>
    <polygon points="300,0 345,0 0,290 0,250" fill="url(#redGrad)"/>
    <polygon points="345,0 362,0 0,305 0,290" fill="#6e0a10"/>
    <polygon points="540,0 840,0 840,250" fill="#141414"/>
    <polygon points="495,0 540,0 840,250 840,290" fill="url(#redGrad)"/>
    <polygon points="478,0 495,0 840,290 840,305" fill="#6e0a10"/>
    <polygon points="0,438 420,420 420,432 0,450" fill="#ec1f27"/>
    <rect x="420" y="440" width="420" height="8" fill="#ec1f27"/>
    <line x1="420" y1="0" x2="420" y2="500" stroke="#c9c9c9" stroke-width="1"/>
    <path role="img" aria-label="Photograph of a two-storey brick office building with a parking lot at sunset"
          d="M420,6 L658,212 Q676,228 658,244 L436,372 Q420,382 404,372 L182,244 Q164,228 182,212 Z"
          fill="url(#photoGrad)" stroke="#ffffff" stroke-width="6" stroke-linejoin="round"/>
  </svg>

  <div class="specialties">
    <p class="specialties__title">SPECIALIZING IN HI-RISES &amp; COMMERCIAL</p>
    <ul class="specialties__list">
      <li><svg class="tick" viewBox="0 0 10 10"><circle cx="5" cy="5" r="4.2" fill="none" stroke="#ec1f27"/><path d="M3 5l1.5 1.5L7.5 3.5" fill="none" stroke="#ec1f27" stroke-width="1.2"/></svg>Concrete Restoration</li>
      <li><svg class="tick" viewBox="0 0 10 10"><circle cx="5" cy="5" r="4.2" fill="none" stroke="#ec1f27"/><path d="M3 5l1.5 1.5L7.5 3.5" fill="none" stroke="#ec1f27" stroke-width="1.2"/></svg>Waterproofing</li>
      <li><svg class="tick" viewBox="0 0 10 10"><circle cx="5" cy="5" r="4.2" fill="none" stroke="#ec1f27"/><path d="M3 5l1.5 1.5L7.5 3.5" fill="none" stroke="#ec1f27" stroke-width="1.2"/></svg>Painting</li>
      <li><svg class="tick" viewBox="0 0 10 10"><circle cx="5" cy="5" r="4.2" fill="none" stroke="#ec1f27"/><path d="M3 5l1.5 1.5L7.5 3.5" fill="none" stroke="#ec1f27" stroke-width="1.2"/></svg>Expansion Joints</li>
      <li><svg class="tick" viewBox="0 0 10 10"><circle cx="5" cy="5" r="4.2" fill="none" stroke="#ec1f27"/><path d="M3 5l1.5 1.5L7.5 3.5" fill="none" stroke="#ec1f27" stroke-width="1.2"/></svg>Caulking</li>
      <li><svg class="tick" viewBox="0 0 10 10"><circle cx="5" cy="5" r="4.2" fill="none" stroke="#ec1f27"/><path d="M3 5l1.5 1.5L7.5 3.5" fill="none" stroke="#ec1f27" stroke-width="1.2"/></svg>Deck Coatings</li>
      <li><svg class="tick" viewBox="0 0 10 10"><circle cx="5" cy="5" r="4.2" fill="none" stroke="#ec1f27"/><path d="M3 5l1.5 1.5L7.5 3.5" fill="none" stroke="#ec1f27" stroke-width="1.2"/></svg>Balustrades &amp; Railings</li>
    </ul>
  </div>

  <address class="contact">
    <p class="contact__company">CORVELL'S PAINTING &amp; WATERPROOFING INC.</p>
    <p class="contact__row"><svg class="contact__icon" viewBox="0 0 12 12"><circle cx="6" cy="6" r="6" fill="#ec1f27"/><path d="M6 2.5a2.2 2.2 0 0 0-2.2 2.2C3.8 6.4 6 9.3 6 9.3s2.2-2.9 2.2-4.6A2.2 2.2 0 0 0 6 2.5z" fill="#fff"/></svg>2200 Seabreeze Blvd</p>
    <p class="contact__row contact__row--indent">Pompano Beach, Florida 33060</p>
    <p class="contact__row"><svg class="contact__icon" viewBox="0 0 12 12"><circle cx="6" cy="6" r="6" fill="#ec1f27"/><path d="M4 3l1.2 1.6-.6.8c.4.9 1 1.5 1.9 1.9l.8-.6L9 7.9 8.3 9C6 8.8 3.2 6 3 3.7z" fill="#fff"/></svg>Tel: 954-555-0142</p>
    <p class="contact__row"><svg class="contact__icon" viewBox="0 0 12 12"><circle cx="6" cy="6" r="6" fill="#ec1f27"/><rect x="3.5" y="4.5" width="5" height="4" fill="#fff"/><rect x="4.5" y="3" width="3" height="1.5" fill="#fff"/></svg>Fax: 954-555-0187</p>
    <p class="contact__row"><svg class="contact__icon" viewBox="0 0 12 12"><circle cx="6" cy="6" r="6" fill="#ec1f27"/><rect x="3" y="4" width="6" height="4.2" fill="#fff"/><path d="M3 4l3 2.3L9 4" fill="none" stroke="#ec1f27" stroke-width=".7"/></svg>Email: corvellrestoration@example.com</p>
  </address>

  <p class="web web--back"><svg class="web__globe" viewBox="0 0 22 22"><circle cx="11" cy="11" r="10" fill="#ec1f27"/><path d="M1 11h20M11 1v20M4 5c4 2 10 2 14 0M4 17c4-2 10-2 14 0M11 1c-4 4-4 16 0 20M11 1c4 4 4 16 0 20" fill="none" stroke="#fff" stroke-width="1"/></svg>WWW.CORVELLRESTORATION.COM</p>

  <p class="tagline">Family Owned<br>&amp; Operated</p>
  <svg class="anniversary-seal" viewBox="0 0 70 70" role="img" aria-label="Anniversary seal">
    <circle cx="35" cy="35" r="32" fill="none" stroke="#ec1f27" stroke-width="3"/>
    <circle cx="35" cy="35" r="22" fill="none" stroke="#ec1f27" stroke-width="1.5"/>
  </svg>

  <div class="brand-name">
    <p class="brand-name__main">Corvell's</p>
    <p class="brand-name__sub">Painting &amp; Restoration</p>
  </div>
  <p class="license-band">General Contractor Licensed &amp; Insured CGC4408215</p>
  <p class="web web--front"><svg class="web__globe" viewBox="0 0 22 22"><circle cx="11" cy="11" r="10" fill="#ec1f27"/><path d="M1 11h20M11 1v20M4 5c4 2 10 2 14 0M4 17c4-2 10-2 14 0M11 1c-4 4-4 16 0 20M11 1c4 4 4 16 0 20" fill="none" stroke="#fff" stroke-width="1"/></svg>WWW.CORVELLRESTORATION.COM</p>
</section>

<section class="spread spread--inside" aria-label="Folder inside: pockets and tabbed sheets">
  <div class="panel panel--left">
    <article class="sheet sheet--painting">
      <div class="sheet__tab"><p class="sheet__brand">Corvell's<small>Painting &amp; Restoration</small></p><p class="sheet__title">Painting</p></div>
    </article>
    <article class="sheet sheet--restoration">
      <div class="sheet__tab"><p class="sheet__brand">Corvell's<small>Painting &amp; Restoration</small></p><p class="sheet__title">Restoration</p></div>
    </article>
    <article class="sheet sheet--deck">
      <div class="sheet__tab"><p class="sheet__brand">Corvell's<small>Painting &amp; Restoration</small></p><p class="sheet__title">Deck, Floor &amp; Epoxy</p></div>
      <h2 class="sheet__heading">Company Background</h2>
      <p class="sheet__text">Lorem ipsum is simply dummy text of the printing and typesetting industry. Lorem Ipsum has been the industry's standard dummy text ever since the 1500s, when an unknown printer took a galley of type and scrambled it to make a type specimen book. It has survived not only five centuries, but also the leap into electronic typesetting, remaining essentially unchanged. It was popularised in the 1960s with the release of Letraset sheets containing Lorem Ipsum passages, and more recently with desktop publishing software including versions of Lorem Ipsum. Lorem Ipsum is simply dummy text of the printing and typesetting industry.</p>
      <div class="sheet__photo" role="img" aria-label="Photograph of a modern high-rise residential tower with balconies against a blue sky"></div>
    </article>
    <div class="pocket">
      <div class="card card--promo">
        <p class="card__name">Corvell's<span>Painting &amp; Restoration</span></p>
        <p class="card__tag">Family Owned &amp; Operated</p>
        <span class="card__dot"></span>
        <p class="card__list"><b>SPECIALIZING IN HI-RISES &amp; COMMERCIAL</b><br>CONCRETE RESTORATION | WATERPROOFING | PAINTING | EXPANSION JOINTS<br>CAULKING | DECK COATINGS | BALUSTRADES &amp; RAILINGS</p>
      </div>
    </div>
  </div>

  <div class="panel panel--right">
    <div class="tab tab--waterproofing">Waterproofing and Deck Systems</div>
    <div class="tab tab--concrete">Concrete Restoration</div>
    <div class="tab tab--painting">Painting</div>
    <div class="tab tab--railing">Railing Systems</div>
    <div class="tab tab--intro">Intro</div>
    <article class="intro-sheet">
      <h2 class="sheet__heading">Company Background</h2>
      <p class="sheet__text">Lorem ipsum is simply dummy text of the printing and typesetting industry. Lorem Ipsum has been the industry's standard dummy text ever since the 1500s, when an unknown printer took a galley of type and scrambled it to make a type specimen book. It has survived not only five centuries, but also the leap into electronic typesetting, remaining essentially unchanged.</p>
      <div class="sheet__photo" role="img" aria-label="Photograph of a curved glass office tower under a blue sky"></div>
    </article>
    <div class="pocket">
      <div class="card card--contact">
        <svg class="card__wedge" viewBox="0 0 192 104" aria-hidden="true">
          <polygon points="0,0 70,0 90,104 0,104" fill="#ec1f27"/>
          <polygon points="70,0 80,0 100,104 90,104" fill="#a3111a"/>
        </svg>
        <p class="card__person">Daniel Corvell<small>Supervisor / Owner<br>General Contractor<br>Licensed &amp; Insured<br>CGC4408215</small></p>
        <p class="card__name">Corvell's<span>Painting &amp; Restoration</span></p>
        <p class="card__details"><i></i>2200 Seabreeze Blvd Pompano<br><i></i>Beach FL 33060<br><i></i>954-555-0142<br><i></i>954-555-0163<br><i></i>corvellrestoration@example.com<br><i></i>www.corvellrestoration.com</p>
      </div>
    </div>
  </div>
</section>

<p class="board-label">FOLDER DESIGN</p>
<div class="board-brand">
  <p class="board-brand__main">Corvell's</p>
  <p class="board-brand__sub">Painting &amp; Restoration</p>
</div>

</body>
</html>
```